Business Card for Fashion House

We need a business card design for our personalize fashion service for our customers. the business card should reflect reliability, luxury and creativity.
The brand Gravetto is extracted from "Graceful Vetto"; Gravetto provides fashion designs sprinkled with luxury and style tailored for our elite clients character profile.
Gravetto is created for those who embody class and elegance with a passion for style.
Target Market(s)
Affluent Customers
Industry/Entity Type
Fashion
Contact Information for Business Card
Rania Bou Khalil
Fashion Designer
Telephone: +971 5550123
Mobile +971 555987
Emal q@z.com
Website www.gravetto-example.com
Social Media Youtube g+ Facebook Instagram Pin /gravetto
Font styles to use
Other font styles liked:
- Audrey provided
Look and feel
Each slider illustrates characteristics of the customer's brand and the style your logo design should communicate.

```html
<!DOCTYPE html>
<html lang="en">
<head>
<meta charset="utf-8">
<title>Gravetto — Business Card</title>
<link rel="stylesheet" href="https://fonts.googleapis.com/css2?family=Marcellus&display=swap">
<style>
  :root {
    --backdrop: #141414;
    --card-white: #f7f7f7;
    --card-black: #0c0c0c;
    --ink: #1a1a1a;
    --ink-soft: #3a3a3a;
    --paper: #ffffff;
  }
  html, body {
    margin: 0;
    padding: 0;
    width: 1200px;
    height: 864px;
    overflow: hidden;
    background: var(--backdrop);
    font-family: "Marcellus", serif;
  }
  .canvas {
    position: relative;
    width: 1200px;
    height: 864px;
  }
  .card {
    position: absolute;
    top: 282px;
    width: 520px;
    height: 300px;
    box-sizing: border-box;
    box-shadow: 0 12px 30px rgba(0,0,0,.6);
  }
  /* Contact side */
  .card--contact {
    left: 50px;
    background: var(--card-white);
    color: var(--ink);
    padding: 34px 40px;
  }
  .brand {
    display: flex;
    align-items: center;
    gap: 12px;
    margin-bottom: 26px;
  }
  .brand__mark {
    width: 12px;
    height: 12px;
    background: var(--ink);
  }
  .brand__name {
    font-size: 20px;
    letter-spacing: .38em;
    text-transform: uppercase;
  }
  .person__name {
    font-size: 17px;
    letter-spacing: .02em;
    text-transform: uppercase;
    margin: 0;
  }
  .person__role {
    font-size: 13px;
    color: var(--ink-soft);
    margin: 2px 0 22px;
  }
  .contacts {
    list-style: none;
    margin: 0;
    padding: 0;
    font-size: 14px;
    letter-spacing: .04em;
  }
  .contacts li {
    display: flex;
    align-items: center;
    gap: 10px;
    height: 20px;
  }
  .contacts svg {
    width: 13px;
    height: 13px;
    flex: none;
  }
  .contacts .contacts__web { font-size: 12px; }
  /* Brand side */
  .card--brand {
    left: 630px;
    background: linear-gradient(135deg, #1c1c1c 0%, var(--card-black) 55%, #050505 100%);
    color: var(--paper);
    display: flex;
    align-items: center;
    justify-content: center;
    gap: 16px;
  }
  .card--brand .brand__mark { background: var(--paper); width: 16px; height: 16px; }
  .card--brand .brand__name { font-size: 28px; }
</style>
</head>
<body>
<main class="canvas">
  <section class="card card--contact" aria-label="Contact side">
    <div class="brand">
      <span class="brand__mark"></span>
      <span class="brand__name">Gravetto</span>
    </div>
    <h1 class="person__name">Rania Bou Khalil</h1>
    <p class="person__role">Fashion Designer</p>
    <ul class="contacts">
      <li>
        <svg viewBox="0 0 14 14" aria-hidden="true"><circle cx="7" cy="7" r="6.3" fill="none" stroke="currentColor"/><path d="M4 5.2c0-.8 1-1.2 3-1.2s3 .4 3 1.2v.6H8.6V5H5.4v.8H4zM4.8 6.5h4.4L10 10H4z" fill="currentColor"/></svg>
        <span>+971 5550123</span>
      </li>
      <li>
        <svg viewBox="0 0 14 14" aria-hidden="true"><circle cx="7" cy="7" r="6.3" fill="none" stroke="currentColor"/><rect x="5" y="3.3" width="4" height="7.4" rx=".7" fill="none" stroke="currentColor"/></svg>
        <span>+971 555987</span>
      </li>
      <li>
        <svg viewBox="0 0 14 14" aria-hidden="true"><circle cx="7" cy="7" r="6.3" fill="none" stroke="currentColor"/><rect x="3.8" y="4.8" width="6.4" height="4.4" fill="none" stroke="currentColor"/><path d="M3.8 4.8L7 7.4l3.2-2.6" fill="none" stroke="currentColor"/></svg>
        <span>q@z.com</span>
      </li>
      <li class="contacts__web">
        <svg viewBox="0 0 14 14" aria-hidden="true"><circle cx="7" cy="7" r="6.3" fill="currentColor"/><g fill="none" stroke="#f7f7f7" stroke-width=".8"><circle cx="7" cy="7" r="4"/><ellipse cx="7" cy="7" rx="1.7" ry="4"/><path d="M3 7h8"/></g></svg>
        <span>www.gravetto-example.com</span>
      </li>
    </ul>
  </section>

  <section class="card card--brand" aria-label="Brand side">
    <span class="brand__mark"></span>
    <span class="brand__name">Gravetto</span>
  </section>
</main>
</body>
</html>
```